Lumigrove Pages with Bold Font

I want the font to be simple yet bold for Lumigrove images. Its all about a simple bold readable font. I need a single lumigrove page with an image and copy/text on or over the image. The words will change in the future. I'm looking for the right font. I like fiery red and yellow colors. The "One Pic" attached is a sample of what I want without the Velnor words.

```html
<!DOCTYPE html>
<html lang="en">
<head>
<meta charset="utf-8">
<title>Lumigrove Page – Bold Type</title>
<link rel="stylesheet" href="https://fonts.googleapis.com/css2?family=Roboto+Condensed:wght@500;700&display=swap">
<style>
  :root {
    --ink-white: #ffffff;
    --fire-yellow: #f7c21a;
    --fire-red: #e5141c;
    --shadow-deep: #17110e;
    --shadow-warm: #3a2a22;
    --tone-skin: #b8866a;
    --tone-light: #d9b49a;
  }
  html, body {
    margin: 0;
    padding: 0;
    width: 1200px;
    height: 1200px;
    overflow: hidden;
    background: var(--shadow-deep);
  }
  .page {
    position: relative;
    width: 1200px;
    height: 1200px;
    overflow: hidden;
    font-family: "Roboto Condensed", "Arial Narrow", sans-serif;
  }
  .hero-photo {
    position: absolute;
    inset: 0;
    background:
      radial-gradient(ellipse 38% 60% at 70% 55%, var(--tone-light) 0%, var(--tone-skin) 45%, rgba(58,42,34,0) 100%),
      radial-gradient(ellipse 50% 45% at 88% 92%, #d8d2cc 0%, rgba(216,210,204,0) 70%),
      linear-gradient(90deg, var(--shadow-deep) 0%, var(--shadow-warm) 45%, #6b4d3d 75%, #4a362c 100%);
  }
  .copy {
    position: absolute;
    left: 41px;
    margin: 0;
  }
  .intro {
    top: 58px;
    font-weight: 500;
    font-size: 38px;
    line-height: 64px;
    color: var(--ink-white);
  }
  .pitch {
    top: 448px;
    font-weight: 700;
    font-size: 66px;
    line-height: 84px;
    color: var(--fire-yellow);
  }
  .promise {
    top: 808px;
    font-weight: 700;
    font-size: 74px;
    line-height: 89px;
    color: var(--fire-red);
  }
</style>
</head>
<body>
  <main class="page">
    <div class="hero-photo" role="img" aria-label="Photograph of a fit woman posing in beige underwear on a bed, lit warmly against a dark room"></div>

    <p class="copy intro">
      As a fitness trainer for men<br>
      I figured if you wanted<br>
      Tits &amp; Ass I’d give it to you.<br>
      At least long enough to make<br>
      a buck and get my guys in shape.
    </p>

    <p class="copy pitch">
      You wanna lose weight?<br>
      You wanna shrink that gut?<br>
      Touch me down here.
    </p>

    <p class="copy promise">
      I can help you<br>
      shrink your gut.
    </p>
  </main>
</body>
</html>
```